One of Australia's fastest growing Financial Company looking for an updated business card design!

Meridale Holdings Australia is looking for an updated design for our business cards. We would like to keep up our professional appearances and have get new exciting design that fits our company.

The Meridale aim is to facilitate and assist clients in every financial requirement that may arise in financial areas.

We would to see the design to use colour blue and we like the clouds in the background. We have attached two designs we have use before but we need something with more professional and easy to read design.

We would like the website in the back of the card; the employees name more central and stands out; only a postal address; a list of all our locations along the bottom (Sydney, Melbourne, Brisbane, Singapore)

Looking forward to seeing the designs come in!

Target Market(s)

Other Industry Professionals
Middle Class Families

Industry/Entity Type

Finance

Contact Information for Business Card

Name; Company Role; Office Number; Mobile Number; Email Address; Website; Postal Address; Locations

Font styles to use
Serif
Sans Serif

Colors
0492cd
33a6d7
85cae6
85acd3
3176b5
0455a3
cee9f5
d5e2ee

Requirements
Must have
• Name; Company Role; Office Number; Mobile Number; Email Address; Website; Postal Address; Locations
Nice to have
• The colour blue, clouds on the background

```html
<!DOCTYPE html>
<html lang="en">
<head>
<meta charset="utf-8">
<title>Meridale Holdings Australia – Business Card</title>
<link rel="stylesheet" href="https://fonts.googleapis.com/css2?family=Open+Sans:ital,wght@0,400;0,600;0,700;1,400&display=swap">
<style>
  :root {
    --stage: #3c3c3c;
    --card-white: #ffffff;
    --brand-blue: #1a82c8;
    --brand-red: #e8383d;
    --text-grey: #555555;
    --back-light: #2ea3dc;
    --back-dark: #1873bd;
    --white: #ffffff;
  }
  * { margin: 0; padding: 0; box-sizing: border-box; }
  html, body {
    width: 1105px;
    height: 1200px;
    overflow: hidden;
    background: var(--stage);
    font-family: "Open Sans", Arial, sans-serif;
  }
  .canvas { position: relative; width: 1105px; height: 1200px; }

  .card {
    position: absolute;
    left: 196px;
    width: 720px;
    height: 412px;
  }
  .card--front { top: 146px; background: var(--card-white); }
  .card--back {
    top: 602px;
    background: radial-gradient(ellipse at 50% 40%, var(--back-light) 0%, var(--back-dark) 75%);
  }

  .holder { position: absolute; right: 30px; top: 22px; text-align: right; }
  .holder__name { font-size: 29px; font-weight: 600; color: var(--brand-blue); line-height: 38px; }
  .holder__role { font-size: 21px; font-weight: 400; color: var(--brand-red); line-height: 24px; }
  .accent-bar { position: absolute; right: 0; top: 29px; width: 10px; height: 61px; background: var(--brand-blue); }

  .brand { position: absolute; left: 32px; top: 146px; display: flex; align-items: center; gap: 16px; }
  .brand__dot { width: 58px; height: 58px; border-radius: 50%; background: var(--brand-red); }
  .brand__name { font-size: 78px; font-weight: 600; color: var(--brand-blue); line-height: 1; letter-spacing: -1px; }

  .contact { position: absolute; left: 32px; top: 280px; font-size: 19px; line-height: 27.5px; color: var(--text-grey); }
  .contact__label { color: var(--brand-blue); font-weight: 600; }

  .address { position: absolute; right: 30px; top: 280px; text-align: right; font-size: 19px; line-height: 27.5px; color: var(--text-grey); }
  .locations { font-style: italic; }
  .locations__dot {
    display: inline-block; width: 8px; height: 8px; border-radius: 50%;
    background: var(--brand-blue); margin: 0 8px; vertical-align: middle;
  }

  .back-brand {
    position: absolute; left: 0; right: 0; top: 162px; text-align: center;
    font-size: 70px; font-weight: 600; color: var(--white); line-height: 1;
  }
  .back-web {
    position: absolute; left: 0; right: 0; top: 338px; text-align: center;
    font-size: 20px; letter-spacing: 3px; color: var(--white);
  }
</style>
</head>
<body>
<main class="canvas">
  <section class="card card--front">
    <div class="holder">
      <p class="holder__name">Clara Bennett</p>
      <p class="holder__role">Investment Consultant</p>
    </div>
    <div class="accent-bar"></div>

    <div class="brand">
      <span class="brand__dot"></span>
      <span class="brand__name">Meridale</span>
    </div>

    <div class="contact">
      <p><span class="contact__label">Phone :</span> (02) 6500 1284</p>
      <p><span class="contact__label">Mobile :</span> 0400 518 2739</p>
      <p>info@meridaleholdingsgroup.com.au</p>
      <p>www.meridaleholdingsgroup.com.au</p>
    </div>

    <div class="address">
      <p>58 Ridgeway Road</p>
      <p>Port Calloway, NSW 2481</p>
      <p class="locations">Sydney<span class="locations__dot"></span>Melbourne</p>
      <p class="locations">Brisbane<span class="locations__dot"></span>Singapore</p>
    </div>
  </section>

  <section class="card card--back">
    <p class="back-brand">Meridale</p>
    <p class="back-web">www.meridaleholdingsgroup.com.au</p>
  </section>
</main>
</body>
</html>
```